Gardener needs an exciting new flyer design.

I'm a passionate gardener that requires a custom flyer design for a owner operator gardening business. Design will be for a DL flyer. I'm based on the Sunshine coast in Queensland Australia. My target audience is the residential market on the Sunshine coast. Business name is Marlowe Greens. My services are, lawn mowing, weeding, Eco Friendly fertilizing, green waste removal, Mulching, tree and shrub pruning, Full garden makeovers, hedging, pressure cleaning, privacy screening, Timber deck rejuvenation, Planting, Turf preparation and installation, and much more. Free no obligation quotes, reliable and friendly service, great rates. 12 years experience. Web www.marlowegreens.com.au - Phone 0418527064 - Email doug@marlowegreens.com.au I would like the design to portray a friendly and professional approach.

Target Market(s)

Residential

Industry/Entity Type

Gardener

Font styles to use
Serif

Colors
9ccb3b
abd037
3176b5

Requirements
Must have
• my services, my logo, my contact details,

```html
<!DOCTYPE html>
<html lang="en">
<head>
<meta charset="utf-8">
<title>Marlowe Greens – DL Flyer</title>
<link href="https://fonts.googleapis.com/css2?family=Montserrat:wght@400;500;700;800&family=Roboto+Slab:wght@400;700&family=Lobster&display=swap" rel="stylesheet">
<style>
  :root{
    --bg:#a8a8a8;
    --label:#3a3a3a;
    --green:#7cc242;
    --green-lite:#9ccb3b;
    --green-dark:#3e8a1e;
    --green-deep:#2f6e17;
    --purple:#5c2266;
    --ink:#2e2e2e;
    --text:#3b3b3b;
    --paper:#ffffff;
    --bar:#2d2d2d;
    --rule:#cfe3b8;
  }
  *{box-sizing:border-box;margin:0;padding:0}
  html,body{width:1200px;height:1181px;overflow:hidden;background:var(--bg)}
  body{position:relative;font-family:"Montserrat",sans-serif;color:var(--text)}
  .side-label{position:absolute;top:58px;font:700 26px "Montserrat",sans-serif;color:var(--label);letter-spacing:.5px}
  .panel{position:absolute;top:100px;width:467px;height:992px;background:var(--paper);overflow:hidden;box-shadow:0 2px 8px rgba(0,0,0,.25)}
  .panel--front{left:103px}
  .panel--back{left:646px}
  .abs{position:absolute}
  .layer{position:absolute;left:0;top:0}
  .center{left:0;right:0;text-align:center}

  /* front */
  .brand-mark{left:202px;top:45px;width:62px;height:62px;border-radius:50%;background:var(--green)}
  .brand-name{top:148px;font:700 34px "Roboto Slab",serif;color:var(--green-deep)}
  .welcome{top:672px;font:400 34px "Roboto Slab",serif;color:var(--green)}
  .welcome-name{top:708px;font:700 40px "Roboto Slab",serif;color:var(--purple)}
  .intro{top:758px;left:20px;right:20px;text-align:center;font:400 16.5px/20px "Montserrat",sans-serif;color:var(--text)}
  .intro b{color:var(--green);font-weight:700}
  .tagline{top:852px;font:400 22px "Lobster",cursive;color:var(--purple)}
  .badge-text{left:343px;top:596px;width:106px;text-align:center;font:400 30px/28px "Lobster",cursive;color:var(--green-deep)}
  .badge-text small{display:block;font-size:13px;line-height:14px;color:#fff}

  /* contact strip */
  .call-note{left:46px;top:933px;font:400 11.5px "Montserrat",sans-serif;color:#fff}
  .call-note b{font-weight:700}
  .phone-icon{left:17px;top:940px}
  .phone-num{left:44px;top:944px;font:800 28px "Montserrat",sans-serif;color:#fff;letter-spacing:.3px}
  .contact-pill{left:243px;top:947px;width:224px;height:28px;background:var(--bar);border-radius:14px 0 0 14px;color:#fff;font:500 12px/28px "Montserrat",sans-serif;padding-left:32px}
  .contact-pill svg{position:absolute;left:6px;top:4px}

  /* back */
  .services-watermark{top:22px;font:700 70px "Roboto Slab",serif;color:rgba(255,255,255,.4);letter-spacing:1px}
  .heading{font:800 33px/33px "Montserrat",sans-serif;color:var(--ink);text-align:center;left:0;right:0}
  .heading .hl{color:var(--green)}
  .service{position:absolute;font:500 17px/21px "Montserrat",sans-serif;color:var(--ink);padding-left:32px;padding-bottom:5px;border-bottom:1px solid var(--rule)}
  .service::before{content:"";position:absolute;left:0;top:2px;width:15px;height:15px;border-radius:50%;background:var(--green)}
  .service::after{content:"";position:absolute;left:4px;top:5px;width:4px;height:7px;border:solid #fff;border-width:0 2px 2px 0;transform:rotate(45deg)}
  .service.last{border-bottom:0}
  .promise{left:32px;top:685px;font:400 22px/27px "Lobster",cursive;color:var(--purple)}
  .promise span{color:var(--green-dark)}
  .owner-name{left:26px;top:810px;font:700 26px "Roboto Slab",serif;color:#fff}
  .owner-bio{left:27px;top:848px;width:225px;font:400 9.2px/12px "Montserrat",sans-serif;color:#fff}
</style>
</head>
<body>

<div class="side-label" style="left:103px">FRONT</div>
<div class="side-label" style="left:646px">BACK</div>

<!-- FRONT PANEL -->
<section class="panel panel--front">
  <svg class="layer" width="467" height="992" viewBox="0 0 467 992">
    <defs>
      <linearGradient id="gardenPhoto" x1="0" y1="0" x2="0" y2="1">
        <stop offset="0" stop-color="#dfe6e8"/>
        <stop offset=".35" stop-color="#4f7a34"/>
        <stop offset=".62" stop-color="#7b8c3c"/>
        <stop offset=".72" stop-color="#4e9a2a"/>
        <stop offset="1" stop-color="#3f8f22"/>
      </linearGradient>
      <linearGradient id="grassBand" x1="0" y1="0" x2="0" y2="1">
        <stop offset="0" stop-color="#6fbf2e"/>
        <stop offset="1" stop-color="#9ccb3b"/>
      </linearGradient>
      <radialGradient id="houseFill" cx=".5" cy=".4" r=".6">
        <stop offset="0" stop-color="#a9cbe9"/><stop offset=".5" stop-color="#6f9a4d"/><stop offset="1" stop-color="#4f8f2f"/>
      </radialGradient>
      <radialGradient id="pathFill" cx=".5" cy=".5" r=".6">
        <stop offset="0" stop-color="#a58fc9"/><stop offset="1" stop-color="#3f7a2c"/>
      </radialGradient>
    </defs>
    <rect x="0" y="110" width="467" height="600" fill="url(#gardenPhoto)" role="img" aria-label="Photo of a landscaped garden with lawn, flower beds and tall trees"/>
    <path d="M0 0H467V150Q300 230 200 220Q80 205 0 120Z" fill="#fff"/>
    <path d="M0 120Q80 205 200 220Q300 230 467 150V160Q300 250 190 230Q70 210 0 130Z" fill="var(--green)"/>
    <path d="M0 655Q150 620 300 640Q400 655 467 700V992H0Z" fill="#fff"/>
    <path d="M0 630Q150 590 300 615Q410 635 467 705V718Q410 650 300 630Q150 605 0 648Z" fill="var(--green-lite)"/>
    <circle cx="106" cy="576" r="86" fill="var(--green)"/>
    <circle cx="106" cy="576" r="75" fill="url(#houseFill)" role="img" aria-label="Photo of a cottage with a tidy front lawn and hedges"/>
    <circle cx="271" cy="574" r="66" fill="var(--green)"/>
    <circle cx="271" cy="574" r="57" fill="url(#pathFill)" role="img" aria-label="Photo of a stone path through lavender beds"/>
    <circle cx="396" cy="631" r="54" fill="var(--green-dark)"/>
    <circle cx="396" cy="631" r="48" fill="var(--green)"/>
    <path d="M0 900Q60 880 120 895T240 892T360 890T467 885V992H0Z" fill="url(#grassBand)"/>
  </svg>
  <div class="abs brand-mark"></div>
  <div class="abs center brand-name">Marlowe Greens</div>
  <div class="abs badge-text">12<br>years<small>Experience.</small></div>
  <div class="abs center welcome">WELCOME TO</div>
  <div class="abs center welcome-name">MARLOWE GREENS</div>
  <p class="abs intro"><b>Marlowe Greens</b> is your garden and lawn care specialist, with a passion for gardening and a keen eye for detail you can rest assured you're in the right hands.</p>
  <div class="abs center tagline">A Beautiful Garden Doesn't Happen By Itself</div>
  <svg class="abs phone-icon" width="22" height="36" viewBox="0 0 22 36"><rect x="2" y="1" width="18" height="34" rx="3" fill="none" stroke="#fff" stroke-width="2.5"/><circle cx="11" cy="30" r="1.6" fill="#fff"/></svg>
  <div class="abs call-note">For More Details, <b>Call Us Today</b></div>
  <div class="abs phone-num">0418 527 064</div>
  <div class="abs contact-pill">
    <svg width="20" height="20" viewBox="0 0 20 20" fill="none" stroke="var(--green)" stroke-width="1.5"><circle cx="10" cy="10" r="8.5"/><ellipse cx="10" cy="10" rx="3.5" ry="8.5"/><path d="M1.5 10H18.5M3 5.5H17M3 14.5H17"/></svg>
    www.marlowegreens.com.au
  </div>
</section>

<!-- BACK PANEL -->
<section class="panel panel--back">
  <svg class="layer" width="467" height="992" viewBox="0 0 467 992">
    <defs>
      <linearGradient id="parkPhoto" x1="0" y1="0" x2="0" y2="1">
        <stop offset="0" stop-color="#4b5a3c"/><stop offset=".6" stop-color="#5f7a3a"/><stop offset="1" stop-color="#3d7a22"/>
      </linearGradient>
      <linearGradient id="footerGreen" x1="0" y1="0" x2="0" y2="1">
        <stop offset="0" stop-color="#3e8a1e"/><stop offset=".7" stop-color="#5aa82a"/><stop offset="1" stop-color="#9ccb3b"/>
      </linearGradient>
      <linearGradient id="portraitFill" x1="0" y1="0" x2="0" y2="1">
        <stop offset="0" stop-color="#8a6a52"/><stop offset="1" stop-color="#3a3230"/>
      </linearGradient>
    </defs>
    <rect x="0" y="0" width="467" height="200" fill="url(#parkPhoto)" role="img" aria-label="Photo of a garden with trees, shrubs and flower beds"/>
    <path d="M0 195Q200 100 467 155V992H0Z" fill="#fff"/>
    <path d="M0 185Q200 90 467 145V160Q200 105 0 195Z" fill="var(--green-lite)"/>
    <path d="M0 792Q80 775 160 790T300 785T467 780V992H0Z" fill="url(#footerGreen)"/>
    <circle cx="357" cy="822" r="92" fill="var(--green-lite)"/>
    <circle cx="357" cy="822" r="82" fill="url(#portraitFill)" role="img" aria-label="Portrait photo of the owner, Doug Marlowe"/>
  </svg>
  <div class="abs center services-watermark">SERVICES</div>
  <div class="abs heading" style="top:157px"><span class="hl">GARDEN</span><br>SERVICES</div>

  <div class="service" style="left:51px;top:250px;width:180px">Lawn mowing</div>
  <div class="service" style="left:51px;top:280px;width:180px">Turf preparation and installation</div>
  <div class="service" style="left:51px;top:330px;width:180px">Tree and shrub pruning</div>
  <div class="service" style="left:51px;top:381px;width:180px">Fertilizing</div>
  <div class="service last" style="left:51px;top:411px;width:180px">Full garden makeovers</div>
  <div class="service" style="left:261px;top:250px;width:170px">Green waste removal</div>
  <div class="service" style="left:261px;top:301px;width:170px">Garden Mulching</div>
  <div class="service" style="left:261px;top:351px;width:170px">Hedging</div>
  <div class="service last" style="left:261px;top:381px;width:170px">Weeding</div>

  <div class="abs heading" style="top:478px"><span class="hl">OTHER</span> SERVICES</div>
  <div class="service" style="left:51px;top:531px;width:300px">luminium fencing and gate installation and repairs</div>
  <div class="service" style="left:51px;top:585px;width:300px">Timber decking rejuvenation and repairs</div>
  <div class="service last" style="left:51px;top:640px;width:330px">Pressure cleaning And much more!</div>

  <div class="abs promise">Free no obligation quotes,<br><span>reliable and friendly service<br>great rates.</span></div>

  <div class="abs owner-name">Doug Marlowe</div>
  <p class="abs owner-bio">From the beautiful Sunshine coast. Doug has over 7 years of experience in gardening and lawn care . With a deep passion in Horticulture you know your in the right hands.</p>

  <svg class="abs phone-icon" width="22" height="36" viewBox="0 0 22 36"><rect x="2" y="1" width="18" height="34" rx="3" fill="none" stroke="#fff" stroke-width="2.5"/><circle cx="11" cy="30" r="1.6" fill="#fff"/></svg>
  <div class="abs call-note">For More Details, <b>Call Us Today</b></div>
  <div class="abs phone-num">0418 527 064</div>
  <div class="abs contact-pill">
    <svg width="20" height="20" viewBox="0 0 20 20"><circle cx="10" cy="10" r="9" fill="var(--green)"/><rect x="5" y="6.5" width="10" height="7" fill="none" stroke="#fff" stroke-width="1.2"/><path d="M5 6.5L10 10.5L15 6.5" fill="none" stroke="#fff" stroke-width="1.2"/></svg>
    doug@marlowegreens.com.au
  </div>
</section>

</body>
</html>
```